Artist/Artwork Product Catalog

I need a small brief product catalog to display my art for purchase to my interior designer clients, to purchase for their clients. Should be 5 - 10 pages with art/canvas display mock up pictures. Sections should include About the artist, space for pricing and art titles, Editable Section Names (3 sections-not including previously mentioned sections), Contact info-including social media. I would like modern and simplistic. My art is filled with bright colors and as such want the design of the catalog to be black and white so as not to detract from the art itself. Please refer to my website and instagram for further design resource: www.teroquillbay.com ; @quillbayteros (instagram)
Target Market(s)
Interior Designers, Collectors, Galleries
Industry/Entity Type
Art Gallery
Colors
Designer to choose colors to be used in the design.
Requirements
Must have
- Must have my artwork included in catalog displayed in canvas wall art mock up. Will send files upon acceptance of catalog design. Need to be printer ready upon project completion as well as editable for future changes as needed. Would like a smaller sized catalog, maybe A4.
Nice to have
- Editable for future use. Would love to have new logo integrated into catalog.
Should not have
- No distracting colors or ornate decorative design

```html
<!DOCTYPE html>
<html lang="en">
<head>
<meta charset="utf-8">
<title>teroquillbay — Product Catalog Cover</title>
<link rel="stylesheet" href="https://fonts.googleapis.com/css2?family=Josefin+Sans:wght@300&display=swap">
<style>
  :root {
    --stage: #cbcbcb;
    --paper: #efefed;
    --ink: #3a3a3a;
    --ink-soft: #4a4a4a;
    --on-ink: #f2f2f2;
  }
  * { margin: 0; padding: 0; box-sizing: border-box; }
  html, body {
    width: 1200px;
    height: 699px;
    overflow: hidden;
    background: var(--stage);
  }
  .canvas {
    position: relative;
    width: 1200px;
    height: 699px;
  }
  .cover {
    position: absolute;
    left: 170px;
    top: 46px;
    width: 860px;
    height: 608px;
    background: var(--paper);
    font-family: "Josefin Sans", sans-serif;
    font-weight: 300;
  }
  .brand-band {
    position: absolute;
    left: 0;
    top: 176px;
    width: 540px;
    height: 112px;
    background: var(--ink);
    display: flex;
    align-items: center;
    padding-left: 52px;
    gap: 40px;
  }
  .brand-mark {
    width: 62px;
    height: 62px;
    border: 4px solid var(--on-ink);
    flex: none;
  }
  .brand-name {
    color: var(--on-ink);
    font-size: 46px;
    letter-spacing: 1px;
    line-height: 1;
    padding-top: 8px;
  }
  .catalog-title {
    position: absolute;
    right: 70px;
    top: 376px;
    color: var(--ink-soft);
    font-size: 31px;
    letter-spacing: 3px;
    text-transform: uppercase;
    line-height: 1;
  }
  .edge-tab {
    position: absolute;
    right: 0;
    top: 356px;
    width: 8px;
    height: 46px;
    background: var(--ink);
  }
</style>
</head>
<body>
  <main class="canvas">
    <section class="cover" aria-label="Product catalog front cover">
      <div class="brand-band">
        <span class="brand-mark" aria-hidden="true"></span>
        <span class="brand-name">teroquillbay</span>
      </div>
      <h1 class="catalog-title">Product Catalog</h1>
      <span class="edge-tab" aria-hidden="true"></span>
    </section>
  </main>
</body>
</html>
```